Real Estate Business Card

Our Company, Brindle Real Estate needs a business card design. It will need a spot for our Name, Office Number, Cell number, email, website address. Brindlerealestate.example and Address. Please utilize our logo for the aesthetic feel of the card. We would like something that is noticeable but looks professional.

Please include our company tagline. "Where Good Homes and Easy Moves Find You"

Industry/Entity Type

Business

Requirements
Should not have
• Black colored Font is OK. But other than that no black

```html
<!DOCTYPE html>
<html lang="en">
<head>
<meta charset="utf-8">
<title>Brindle Real Estate – Business Card</title>
<link href="https://fonts.googleapis.com/css2?family=Arimo:wght@400;700&display=swap" rel="stylesheet">
<style>
  :root {
    --backdrop: #2b2b2d;
    --card: #333336;
    --orange: #e8731c;
    --blue: #2a5aa0;
    --white: #f2f2f2;
    --grey: #8a8d92;
  }
  * { margin: 0; padding: 0; box-sizing: border-box; }
  html, body { width: 1200px; height: 1000px; overflow: hidden; }
  body {
    background: var(--backdrop);
    font-family: "Arimo", Arial, sans-serif;
    position: relative;
  }
  .card {
    position: absolute;
    left: 250px;
    width: 700px;
    height: 400px;
    background: var(--card);
    overflow: hidden;
    box-shadow: 0 10px 30px rgba(0,0,0,.45);
  }
  .card--front { top: 70px; }
  .card--back { top: 530px; }

  /* Front */
  .brand {
    position: absolute;
    left: 70px;
    top: 110px;
    display: flex;
    align-items: center;
    gap: 16px;
  }
  .brand__mark { width: 64px; height: 64px; background: var(--orange); flex: none; }
  .brand__name {
    font-weight: 700;
    font-size: 46px;
    color: var(--blue);
    letter-spacing: -0.5px;
    white-space: nowrap;
  }
  .tagline {
    position: absolute;
    left: 150px;
    top: 178px;
    font-weight: 700;
    font-size: 16px;
    color: var(--white);
    white-space: nowrap;
  }
  .front-rule {
    position: absolute; left: 0; right: 0; top: 300px; height: 4px; background: var(--blue);
  }
  .front-band {
    position: absolute; left: 0; right: 0; top: 308px; bottom: 0; background: var(--orange);
  }

  /* Back */
  .back-brand {
    position: absolute;
    left: 40px;
    top: 40px;
    font-weight: 700;
    font-size: 26px;
    color: var(--orange);
    white-space: nowrap;
  }
  .person {
    position: absolute;
    right: 60px;
    top: 40px;
    text-align: right;
  }
  .person__name { font-weight: 700; font-size: 24px; color: var(--blue); }
  .person__title { font-size: 15px; color: var(--grey); margin-top: 2px; }
  .contacts {
    position: absolute;
    right: 30px;
    top: 118px;
    list-style: none;
  }
  .contacts__item {
    display: flex;
    justify-content: flex-end;
    align-items: center;
    gap: 10px;
    height: 26px;
    font-weight: 700;
    font-size: 15px;
    color: var(--orange);
    white-space: nowrap;
  }
  .contacts__item--address { color: var(--white); }
  .contacts__icon { width: 16px; height: 16px; flex: none; }
  .back-rule {
    position: absolute; left: 0; right: 0; top: 300px; height: 3px; background: var(--orange);
  }
  .back-band {
    position: absolute; left: 0; right: 0; top: 306px; bottom: 0; background: var(--blue);
  }
</style>
</head>
<body>
  <section class="card card--front" aria-label="Business card front">
    <div class="brand">
      <span class="brand__mark"></span>
      <span class="brand__name">Brindle Real Estate</span>
    </div>
    <p class="tagline">Where Good Homes and Easy Moves Find You</p>
    <div class="front-rule"></div>
    <div class="front-band"></div>
  </section>

  <section class="card card--back" aria-label="Business card back">
    <div class="back-brand">Brindle Real Estate</div>
    <div class="person">
      <div class="person__name">YOUR NAME</div>
      <div class="person__title">Title</div>
    </div>
    <ul class="contacts">
      <li class="contacts__item contacts__item--address">Name of place, City, Country, NY 1234
        <svg class="contacts__icon" viewBox="0 0 16 16"><path d="M8 1a5 5 0 0 0-5 5c0 4 5 9 5 9s5-5 5-9a5 5 0 0 0-5-5z" fill="#2a5aa0"/><circle cx="8" cy="6" r="2" fill="#333336"/></svg>
      </li>
      <li class="contacts__item">123 56 789
        <svg class="contacts__icon" viewBox="0 0 16 16"><path d="M3 1h3l1 4-2 1a9 9 0 0 0 5 5l1-2 4 1v3a2 2 0 0 1-2 2C7 15 1 9 1 3a2 2 0 0 1 2-2z" fill="#2a5aa0"/></svg>
      </li>
      <li class="contacts__item">123 456 0987
        <svg class="contacts__icon" viewBox="0 0 16 16"><rect x="4" y="1" width="8" height="14" rx="1.5" fill="none" stroke="#2a5aa0" stroke-width="1.6"/><circle cx="8" cy="12.5" r="0.9" fill="#2a5aa0"/></svg>
      </li>
      <li class="contacts__item">123 456 0988
        <svg class="contacts__icon" viewBox="0 0 16 16"><rect x="1" y="3" width="14" height="10" rx="1" fill="#2a5aa0"/><path d="M1.5 3.5 8 9l6.5-5.5" fill="none" stroke="#333336" stroke-width="1.2"/></svg>
      </li>
      <li class="contacts__item">yourname@brindleestate.example
        <svg class="contacts__icon" viewBox="0 0 16 16"><circle cx="8" cy="8" r="6.5" fill="none" stroke="#2a5aa0" stroke-width="1.4"/><ellipse cx="8" cy="8" rx="2.8" ry="6.5" fill="none" stroke="#2a5aa0" stroke-width="1.2"/><path d="M1.5 8h13" stroke="#2a5aa0" stroke-width="1.2"/></svg>
      </li>
      <li class="contacts__item">Brindlerealestate.example
        <span class="contacts__icon"></span>
      </li>
    </ul>
    <div class="back-rule"></div>
    <div class="back-band"></div>
  </section>
</body>
</html>
```